VERIDAX Need a luxury modern business card designed.

Need a luxury modern business card designed. refer to the uploaded files for the company name and logo in the zip file under source files. i will making my descion on monday. so please send in before then so if we need to edit we will have the time. we have a trade show coming up and im on a deadline for printer.

Target Market(s)

high end clients

Contact Information for Business Card

Company nAme and logo. Calvin Ostrow Co-Founder / Project Manager Office # 416-555-0193 Cell # 416-555-0147 VERIDAX.CA Calvin@veridax.ca

Font styles to use
Other font styles liked:
• Modern

Requirements
Must have
• Company name and logo, contact info, using the black, gold and white color scheme.

```html
<!DOCTYPE html>
<html lang="en">
<head>
<meta charset="utf-8">
<title>VERIDAX — Business Card</title>
<link href="https://fonts.googleapis.com/css2?family=Work+Sans:wght@400;500;600&display=swap" rel="stylesheet">
<style>
  :root {
    --stage: #1b1b1b;
    --card: #222222;
    --card-edge: #2c2c2c;
    --gold: #aa9b63;
    --gold-soft: rgba(170, 155, 99, 0.32);
    --gold-faint: rgba(170, 155, 99, 0.08);
    --white: #f4f4f2;
    --silver: #8e8e8e;
  }
  * { box-sizing: border-box; margin: 0; padding: 0; }
  html, body {
    width: 1200px;
    height: 900px;
    overflow: hidden;
    background: var(--stage);
    font-family: "Work Sans", Arial, sans-serif;
  }
  .canvas {
    position: relative;
    width: 1200px;
    height: 900px;
  }
  .card {
    position: absolute;
    left: 250px;
    width: 700px;
    height: 400px;
    background: var(--card);
    border: 1px solid var(--card-edge);
    overflow: hidden;
  }
  .card--back { top: 40px; }
  .card--front { top: 470px; }

  .brand-lockup {
    position: absolute;
    left: 0;
    right: 0;
    top: 112px;
    display: flex;
    flex-direction: column;
    align-items: center;
    gap: 26px;
  }
  .brand-lockup__square {
    width: 44px;
    height: 44px;
    background: var(--silver);
  }

  .wordmark {
    font-weight: 400;
    letter-spacing: 0.28em;
    line-height: 1;
  }
  .card--back .wordmark {
    font-size: 52px;
    color: var(--silver);
    padding-left: 0.28em;
  }
  .card--front .wordmark {
    position: absolute;
    left: 44px;
    top: 44px;
    font-size: 44px;
    color: var(--white);
  }

  .brand-symbol-area {
    position: absolute;
    left: 390px;
    top: 110px;
    width: 270px;
    height: 260px;
    background: linear-gradient(135deg, var(--gold-soft), var(--gold-faint));
  }

  .contact {
    position: absolute;
    left: 44px;
    top: 206px;
    color: var(--white);
  }
  .contact__name {
    font-size: 36px;
    font-weight: 600;
    color: var(--gold);
    letter-spacing: 0.01em;
    line-height: 1.1;
  }
  .contact__role {
    font-size: 18px;
    margin-top: 4px;
    margin-bottom: 16px;
  }
  .contact__line {
    display: flex;
    align-items: center;
    gap: 10px;
    font-size: 19px;
    line-height: 1.5;
  }
  .contact__line svg {
    width: 14px;
    height: 14px;
    flex: none;
    stroke: var(--gold);
    fill: none;
    stroke-width: 1.6;
  }
</style>
</head>
<body>
<main class="canvas">
  <section class="card card--back" aria-label="Card back">
    <div class="brand-lockup">
      <div class="brand-lockup__square"></div>
      <div class="wordmark">VERIDAX</div>
    </div>
  </section>

  <section class="card card--front" aria-label="Card front">
    <div class="wordmark">VERIDAX</div>

    <div class="brand-symbol-area" role="img" aria-label="Large gold and white brand symbol"></div>

    <div class="contact">
      <p class="contact__name">Calvin Ostrow</p>
      <p class="contact__role">Co-Founder</p>
      <p class="contact__line">
        <svg viewBox="0 0 14 14" aria-hidden="true"><path d="M3 1.5 L5 4 L4 5.5 Q5.5 8.5 8.5 10 L10 9 L12.5 11 L11 12.5 Q5 12 1.5 3 Z"/></svg>
        416-555-0193
      </p>
      <p class="contact__line">
        <svg viewBox="0 0 14 14" aria-hidden="true"><rect x="4" y="1" width="6" height="12" rx="1"/><line x1="6.3" y1="11" x2="7.7" y2="11"/></svg>
        416-555-0147
      </p>
      <p class="contact__line">
        <svg viewBox="0 0 14 14" aria-hidden="true"><rect x="1" y="3" width="12" height="8"/><path d="M1 3 L7 8 L13 3"/></svg>
        veridax.ca&nbsp; Calvin@veridax.ca
      </p>
    </div>
  </section>
</main>
</body>
</html>
```